Proposal Form

Hello! We would like a full color (CMYK) form created with our logo and a similar look and feel to other documents we use (attached). Underneath logo and some design (design should be landscaping based as that is what we will be quoting), we would need a bunch of horizontal lines (for us to write on) and a space in the bottom right which has three lines - (1) Project Total _____________ (2) ______ Monthly Payments of _________________ (3) Pre-pay and receive a 3% discount _______________________

```html
<!DOCTYPE html>
<html lang="en">
<head>
<meta charset="utf-8">
<title>Willow Bend – Proposal Form</title>
<link href="https://fonts.googleapis.com/css2?family=Cinzel:wght@400;500&family=Lato:wght@400;700&display=swap" rel="stylesheet">
<style>
  :root{
    --canvas:#eeeeee;
    --ink:#19191b;
    --paper:#ffffff;
    --rule:#bcbcbc;
    --accent-blue:#3f6f97;
    --footer-end:#5e5e60;
    --badge-gold:#c9a62a;
    --badge-green:#2a9d6a;
    --badge-lime:#a7b832;
    --text-dark:#1a1a1a;
  }
  *{box-sizing:border-box;margin:0;padding:0}
  html,body{width:1200px;height:960px;overflow:hidden;background:var(--canvas)}
  body{position:relative;font-family:'Lato',sans-serif}

  .form-sheet{position:absolute;top:165px;width:490px;height:634px;background:var(--paper);overflow:hidden}
  .form-sheet--garden{left:90px}
  .form-sheet--snow{left:620px}

  .sheet-header{position:absolute;left:0;top:0;width:490px;height:150px}
  .sheet-header svg{position:absolute;left:0;top:0}
  .brand-name{position:absolute;left:0;top:52px;width:490px;text-align:center;
    font-family:'Cinzel',serif;font-weight:400;font-size:28px;letter-spacing:7px;color:#fff}

  .writing-rules{position:absolute;left:29px;top:0;width:432px;height:100%}
  .writing-rules .rule{position:absolute;left:0;width:432px;height:1px;background:var(--rule)}
  .writing-rules .rule--title{width:216px}

  .sheet-footer{position:absolute;left:0;top:500px;width:490px;height:134px}
  .sheet-footer svg{position:absolute;left:0;top:0}
  .footer-tagline{position:absolute;left:30px;top:13px;font-family:'Cinzel',serif;font-size:10px;letter-spacing:1px;color:#e8e8e8}
  .footer-title{position:absolute;left:28px;top:22px;font-family:'Cinzel',serif;font-size:38px;letter-spacing:3px;color:#fff;line-height:1}
  .badge-row{position:absolute;left:30px;top:62px;display:flex;gap:16px}
  .badge{width:36px;height:36px}
  .badge--shield{border-radius:4px 4px 18px 18px}
  .badge--round{border-radius:50%}
  .badge--gold{background:var(--badge-gold)}
  .badge--green{background:var(--badge-green)}
  .badge--lime{background:var(--badge-lime)}
  .contact-line{position:absolute;left:21px;top:104px;display:flex;align-items:center;gap:6px;font-size:8.5px;letter-spacing:.8px;color:#e6e6e6}
  .contact-line svg{width:10px;height:10px}

  .pricing-box{position:absolute;left:241px;top:16px;width:224px;height:94px;background:var(--paper);border-radius:8px;padding:0 6px;color:var(--text-dark)}
  .pricing-row{position:absolute;left:5px;right:6px;display:flex;align-items:flex-end;font-size:9px;font-weight:700;letter-spacing:-.2px}
  .pricing-row .blank{flex:1;border-bottom:1px solid #9a9a9a;height:1px;margin-bottom:1px}
  .pricing-row .blank--lead{flex:0 0 55px}
  .pricing-row--total{top:14px}
  .pricing-row--monthly{top:47px}
  .pricing-row--prepay{top:79px;left:7px}
</style>
</head>
<body>

<!-- Garden variant -->
<section class="form-sheet form-sheet--garden">
  <header class="sheet-header">
    <svg width="490" height="150" viewBox="0 0 490 150">
      <defs>
        <linearGradient id="gardenTones" x1="0" x2="1">
          <stop offset="0" stop-color="#7aa048"/>
          <stop offset=".3" stop-color="#b45a6a"/>
          <stop offset=".55" stop-color="#6f8c45"/>
          <stop offset=".8" stop-color="#c06070"/>
          <stop offset="1" stop-color="#8fb35a"/>
        </linearGradient>
      </defs>
      <path role="img" aria-label="Photo of a flower bed with shrubs and lawn" d="M0 120 L490 118 L490 149 Q360 143 240 148 Q120 151 0 149 Z" fill="url(#gardenTones)"/>
      <path d="M0 0 H490 V124 Q340 112 180 122 Q80 127 0 122 Z" fill="var(--ink)"/>
      <path d="M0 124 Q80 129 180 124 Q340 114 490 126" fill="none" stroke="var(--accent-blue)" stroke-width="3"/>
    </svg>
    <div class="brand-name">Willow Bend</div>
  </header>

  <div class="writing-rules">
    <span class="rule rule--title" style="top:193px"></span>
    <span class="rule" style="top:231px"></span>
    <span class="rule" style="top:257px"></span>
    <span class="rule" style="top:281px"></span>
    <span class="rule" style="top:307px"></span>
    <span class="rule" style="top:332px"></span>
    <span class="rule" style="top:357px"></span>
    <span class="rule" style="top:382px"></span>
    <span class="rule" style="top:408px"></span>
    <span class="rule" style="top:433px"></span>
    <span class="rule" style="top:458px"></span>
    <span class="rule" style="top:483px"></span>
  </div>

  <footer class="sheet-footer">
    <svg width="490" height="134" viewBox="0 0 490 134">
      <defs>
        <linearGradient id="footerShade1" x1="0" x2="1">
          <stop offset="0" stop-color="var(--ink)"/>
          <stop offset=".7" stop-color="#2a2a2c"/>
          <stop offset="1" stop-color="var(--footer-end)"/>
        </linearGradient>
      </defs>
      <path d="M0 6 Q240 0 490 4 V134 H0 Z" fill="url(#footerShade1)"/>
    </svg>
    <div class="footer-tagline">Landscaping &amp; Snow Removal</div>
    <div class="footer-title">EXPERTS</div>
    <div class="badge-row">
      <span class="badge badge--shield badge--gold"></span>
      <span class="badge badge--round badge--gold"></span>
      <span class="badge badge--shield badge--lime"></span>
      <span class="badge badge--shield badge--green"></span>
    </div>
    <div class="contact-line">
      <svg viewBox="0 0 10 10"><circle cx="5" cy="5" r="4.5" fill="none" stroke="#e6e6e6" stroke-width=".8"/><path d="M3.3 2.6 L4.2 3.6 L3.8 4.3 Q4.5 5.6 5.7 6.2 L6.4 5.8 L7.4 6.7 L6.8 7.5 Q4.3 7.2 2.6 3.3 Z" fill="#e6e6e6"/></svg>
      <span>(555) 014-2290</span><span>~</span><span>office@willowbend.com</span>
    </div>
    <div class="pricing-box">
      <div class="pricing-row pricing-row--total"><span>Project Total :</span><span class="blank"></span></div>
      <div class="pricing-row pricing-row--monthly"><span class="blank blank--lead"></span><span>Monthly Payments of:</span><span class="blank"></span></div>
      <div class="pricing-row pricing-row--prepay"><span>Pre-pay and receive a 3% discount</span><span class="blank"></span></div>
    </div>
  </footer>
</section>

<!-- Snow variant -->
<section class="form-sheet form-sheet--snow">
  <header class="sheet-header">
    <svg width="490" height="150" viewBox="0 0 490 150">
      <defs>
        <linearGradient id="snowTones" x1="0" x2="1">
          <stop offset="0" stop-color="#3a3a3a"/>
          <stop offset=".25" stop-color="#cfcfcf"/>
          <stop offset=".45" stop-color="#3b3520"/>
          <stop offset=".65" stop-color="#b8902e"/>
          <stop offset=".85" stop-color="#d9d9d9"/>
          <stop offset="1" stop-color="#e6e6e6"/>
        </linearGradient>
      </defs>
      <path role="img" aria-label="Photo of a plow truck clearing snow" d="M0 120 L490 118 L490 149 Q360 143 240 148 Q120 151 0 149 Z" fill="url(#snowTones)"/>
      <path d="M0 0 H490 V124 Q340 112 180 122 Q80 127 0 122 Z" fill="var(--ink)"/>
      <path d="M0 124 Q80 129 180 124 Q340 114 490 126" fill="none" stroke="var(--accent-blue)" stroke-width="3"/>
    </svg>
    <div class="brand-name">Willow Bend</div>
  </header>

  <div class="writing-rules">
    <span class="rule rule--title" style="top:193px"></span>
    <span class="rule" style="top:231px"></span>
    <span class="rule" style="top:257px"></span>
    <span class="rule" style="top:281px"></span>
    <span class="rule" style="top:307px"></span>
    <span class="rule" style="top:332px"></span>
    <span class="rule" style="top:357px"></span>
    <span class="rule" style="top:382px"></span>
    <span class="rule" style="top:408px"></span>
    <span class="rule" style="top:433px"></span>
    <span class="rule" style="top:458px"></span>
    <span class="rule" style="top:483px"></span>
  </div>

  <footer class="sheet-footer">
    <svg width="490" height="134" viewBox="0 0 490 134">
      <defs>
        <linearGradient id="footerShade2" x1="0" x2="1">
          <stop offset="0" stop-color="var(--ink)"/>
          <stop offset=".7" stop-color="#2a2a2c"/>
          <stop offset="1" stop-color="var(--footer-end)"/>
        </linearGradient>
      </defs>
      <path d="M0 6 Q240 0 490 4 V134 H0 Z" fill="url(#footerShade2)"/>
    </svg>
    <div class="footer-tagline">Landscaping &amp; Snow Removal</div>
    <div class="footer-title">EXPERTS</div>
    <div class="badge-row">
      <span class="badge badge--shield badge--gold"></span>
      <span class="badge badge--round badge--gold"></span>
      <span class="badge badge--shield badge--lime"></span>
      <span class="badge badge--shield badge--green"></span>
    </div>
    <div class="contact-line">
      <svg viewBox="0 0 10 10"><circle cx="5" cy="5" r="4.5" fill="none" stroke="#e6e6e6" stroke-width=".8"/><path d="M3.3 2.6 L4.2 3.6 L3.8 4.3 Q4.5 5.6 5.7 6.2 L6.4 5.8 L7.4 6.7 L6.8 7.5 Q4.3 7.2 2.6 3.3 Z" fill="#e6e6e6"/></svg>
      <span>(555) 014-2290</span><span>~</span><span>office@willowbend.com</span>
    </div>
    <div class="pricing-box">
      <div class="pricing-row pricing-row--total"><span>Project Total :</span><span class="blank"></span></div>
      <div class="pricing-row pricing-row--monthly"><span class="blank blank--lead"></span><span>Monthly Payments of:</span><span class="blank"></span></div>
      <div class="pricing-row pricing-row--prepay"><span>Pre-pay and receive a 3% discount</span><span class="blank"></span></div>
    </div>
  </footer>
</section>

</body>
</html>
```